velmorino.eu :: Design ideas (no coding) for key pages of Personalized greeting cards online store

We need your vision on modern, clean, easy to read user interface (UI) for online service of personalized printed products, like greeting cards, postcards, fridge magnets, clips and etc.
Your vision should include UI presentation for:
- Home page with login (including soc nets)
- Product Designer page
- Cart pages (products and address selection)
- Example of general internal page (pricing, terms, etc)
- Artist info and portfolio page
We are looking for ideas we will love, NOT complete design of a whole site.
Top design/vision will we used as a basement for separate contract on complete design of the site.

UI should be based on existing functionality with some extent. It should not break ideas or methods used on prototype but designers are free to offer own product presentations, designer’s layout and cart views.

Prototype:
English: http://velmorino.eu
Russian: http://velmorino.ru
Lithuanian: http://velmorino.lt

Target Market(s)

People of 16-45 y.o. who likes to be distinctive, personal.

Industry/Entity Type

Store

Requirements
Must have
• Your work should meet attached requirements.
Site is multilingual. Wording should assume varieties in length on different languages.
Clean and easy to read UI
Flat design preferrably
Should be based on assets which are free or available for royalty-free licensing
Should not have
• heavy, meaningless 3D and shadow effects
Show NOT copy sites like: plonkra.com, tarnwick.co.uk

```html
<!DOCTYPE html>
<html lang="en">
<head>
<meta charset="utf-8">
<title>velmorino – personalised greeting cards</title>
<link href="https://fonts.googleapis.com/css2?family=Roboto:ital,wght@0,300;0,400;0,500;1,400&family=Roboto+Condensed:ital,wght@0,400;0,700;1,400&family=Ubuntu:wght@300;400;500&display=swap" rel="stylesheet">
<style>
:root{
  --teal:#2aa1a4;
  --teal-dark:#1c8a8e;
  --teal-light:#5fc2c2;
  --red:#d9473d;
  --text:#444;
  --muted:#8a8a8a;
  --line:#c9c9c9;
  --footer:#3d3d3d;
  --green:#7ab93c;
  --aqua:#3bb6a9;
  --blue:#3b86c2;
  --purple:#9b44c0;
}
*{margin:0;padding:0;box-sizing:border-box}
html,body{width:843px;height:1200px;overflow:hidden;background:#fff}
.page{position:relative;width:1000px;height:1424px;transform:scale(.843);transform-origin:0 0;font-family:Roboto,Arial,sans-serif;color:var(--text)}
.abs{position:absolute}

.brand-mark{left:76px;top:20px;width:60px;height:56px;background:var(--teal);border:3px solid var(--red)}
.brand-name{left:73px;top:79px;font:400 17px Ubuntu,sans-serif;color:var(--red)}
.tagline{left:74px;top:105px;font-size:12px;color:var(--red)}
.account{left:668px;top:33px;font-size:14px;color:#444;letter-spacing:.3px}
.account span{margin:0 10px}
.lang{left:845px;top:33px;font-size:12px;display:flex;align-items:center;gap:8px}
.flag{width:28px;height:14px;background:#2b3f8c;border:2px solid #c9323a}
.cart{left:823px;top:86px;font-size:13px;display:flex;align-items:center;gap:10px}

.nav{left:0;top:134px;width:1000px;height:39px;background:var(--teal);border-top:2px solid var(--teal-light);display:flex;padding-left:72px}
.nav a{color:#fff;text-decoration:none;font:400 14px "Roboto Condensed",sans-serif;line-height:37px;padding:0 30px;border-right:1px solid rgba(255,255,255,.2)}
.nav a.active{background:var(--teal-dark);padding:0 24px}

.hero{left:0;top:173px;width:1000px;height:386px;background:radial-gradient(circle at 30% 20%,#1c8d98 0%,#34a7ae 40%,#6cc6c4 75%,#a8d7cf 100%)}
.hero h1{position:absolute;left:155px;top:128px;font:400 30px Ubuntu,sans-serif;color:#fff;white-space:nowrap}
.hero h2{position:absolute;left:155px;top:177px;font:300 21px Ubuntu,sans-serif;color:#fff;white-space:nowrap}
.hero p{position:absolute;left:156px;top:216px;width:370px;font:300 12px/24px Ubuntu,sans-serif;color:#fff;letter-spacing:-.3px}
.hero .arrow{position:absolute;top:158px;width:52px;height:52px;border-radius:50%;background:rgba(60,90,100,.35)}
.hero .cards{position:absolute;left:540px;top:42px;width:300px;height:252px;background:linear-gradient(120deg,#e8b6a8 0%,#d9c7bd 40%,#8f8f8f 70%,#c9c9c9 100%)}

.sidebar-title{left:73px;top:598px;width:188px;height:28px;background:linear-gradient(90deg,#f6a9a0,#fde4e0 80%,#fff);color:#b8483f;font-size:14px;line-height:28px;padding-left:21px;letter-spacing:.5px}
.categories{left:73px;top:635px;width:188px;list-style:none}
.categories li{height:30px;border-bottom:1px dotted #aaa;font-size:11.5px;letter-spacing:-.3px;white-space:nowrap;color:#666;line-height:28px;padding-left:18px;position:relative}
.categories li:last-child{border:none}
.categories li::before{content:"";position:absolute;left:2px;top:10px;border-left:5px solid #222;border-top:4px solid transparent;border-bottom:4px solid transparent}
.testi-title{left:74px;top:889px;font:400 18px Ubuntu,sans-serif;color:#333}
.quote{left:73px;top:930px;width:188px;height:106px;background:#eee;padding:11px 14px 0 21px;font:italic 400 11px/20px "Roboto Condensed",sans-serif;color:#555}
.avatar{left:80px;top:1056px;width:40px;height:42px;border-radius:4px;background:linear-gradient(#8a5a3a,#f1d6c8)}
.author{left:150px;top:1060px;font-size:11px;font-weight:500;color:#333;line-height:23px;white-space:nowrap}

.toolbar{left:323px;top:597px;width:605px;height:62px;background:#fff;box-shadow:0 0 4px rgba(0,0,0,.18);display:flex;align-items:center;padding-left:18px;font-size:14px}
.swatch{position:absolute;top:19px;width:30px;height:25px}

.product{width:190px;height:279px;background:#fff;box-shadow:0 0 3px rgba(0,0,0,.2)}
.product .art{position:absolute;left:7px;top:7px;width:176px;height:152px}
.product h3{position:absolute;left:8px;top:172px;font:400 14px Roboto,sans-serif;color:#555;letter-spacing:.3px;white-space:nowrap}
.product p{position:absolute;left:8px;top:194px;width:180px;font-size:11.5px;line-height:18px;color:#888}
.product .note{position:absolute;left:16px;top:243px}
.product .price{position:absolute;right:22px;top:247px;font-size:14px;color:#444}

.footer{left:0;top:1324px;width:1000px;height:100px;background:var(--footer);color:#fff;font-size:12px}
.footer .links{position:absolute;left:74px;top:28px}
.footer .copy{position:absolute;left:74px;top:58px}
.social{position:absolute;top:34px;width:30px;height:30px}
</style>
</head>
<body>
<div class="page">
  <header>
    <div class="abs brand-mark"></div>
    <div class="abs brand-name">velmorino</div>
    <div class="abs tagline">The individual greeting cards according to your mood</div>
    <div class="abs account">SIGN IN<span>|</span>LOGIN</div>
    <div class="abs lang"><span class="flag"></span>ENGLISH</div>
    <div class="abs cart">
      <svg width="16" height="14" viewBox="0 0 16 14"><path d="M1 1h3l2 8h7l2-6H5" fill="none" stroke="#d9473d" stroke-width="1.5"/><circle cx="7" cy="12" r="1.3" fill="#555"/><circle cx="12" cy="12" r="1.3" fill="#555"/></svg>
      Cart (0) items
    </div>
  </header>

  <nav class="abs nav">
    <a class="active">HOME</a><a>ABOUT US</a><a>BUY NOW</a><a>OUR CATEGORY</a><a>OUR SPECIALS</a><a>AUTHORS</a><a>CONTACT US</a>
  </nav>

  <section class="abs hero">
    <div class="arrow" style="left:73px">
      <svg width="52" height="52"><path d="M30 16 20 26l10 10" fill="none" stroke="#fff" stroke-width="1.5"/></svg>
    </div>
    <h1>Typinon habent claritatem</h1>
    <h2>Duis autem vel eum iriure dolor</h2>
    <p>Ut wisi enim ad minim veniam, quis nostrud exerci tation ullamcor per suscipit lobortis nisl ut aliquip ex ea commodo consequat.</p>
    <div class="cards" role="img" aria-label="Two open greeting cards: a pastel tree illustration and a black-and-white animal photo"></div>
    <div class="arrow" style="left:877px">
      <svg width="52" height="52"><path d="M22 16l10 10-10 10" fill="none" stroke="#fff" stroke-width="1.5"/></svg>
    </div>
  </section>

  <aside>
    <div class="abs sidebar-title">CATEGORIES</div>
    <ul class="abs categories">
      <li>Greeting cards</li><li>Postcards of different size</li><li>Fridge magnets of different szes</li><li>Wooden boards with clip</li><li>T–Shirts</li><li>cups</li><li>Typi non habent</li>
    </ul>
    <div class="abs testi-title">Testimonials</div>
    <div class="abs quote">Fusce feugiat meisuada odio. M orbi nunc dogravida at, rsus ne c, luctus a, lorem. Maecnatristiq ue orci acsem Lorem ipsum.</div>
    <svg class="abs" style="left:215px;top:1036px" width="30" height="16"><path d="M0 0h30L8 16z" fill="#eee"/></svg>
    <div class="abs avatar" role="img" aria-label="Customer portrait"></div>
    <div class="abs author">Maenintty intcoqt<br>
      <svg width="12" height="12" viewBox="0 0 12 12" style="vertical-align:-1px;margin-right:8px"><circle cx="6" cy="3.5" r="3" fill="#555"/><path d="M0 12c0-4 3-5 6-5s6 1 6 5z" fill="#555"/></svg>Dara Wenlock's</div>
  </aside>

  <div class="abs toolbar">
    Themes
    <svg width="12" height="8" style="margin-left:10px"><path d="M1 1h10L6 7z" fill="#333"/></svg>
    <svg class="abs" style="left:152px;top:20px" width="22" height="22" viewBox="0 0 22 22"><g stroke="#c0262b" stroke-width="3"><path d="M11 1v20M2 6l18 10M2 16l18-10"/></g></svg>
    <svg class="abs" style="left:195px;top:20px" width="140" height="24" fill="none" stroke="#c05a50" stroke-width="1">
      <rect x="1" y="5" width="13" height="18"/><rect x="14" y="11" width="22" height="12"/>
      <path d="M58 23V8l8-6v21zM58 8h8"/>
      <rect x="92" y="3" width="15" height="20"/><rect x="107" y="7" width="26" height="16"/>
    </svg>
    <span class="abs" style="left:388px;top:23px">Color</span>
    <div class="swatch" style="left:433px;background:var(--green)"></div>
    <div class="swatch" style="left:472px;background:var(--aqua)"></div>
    <div class="swatch" style="left:511px;background:var(--blue)"></div>
    <div class="swatch" style="left:551px;background:var(--purple)"></div>
  </div>

  <main>
    <article class="abs product" style="left:323px;top:685px">
      <div class="art" role="img" aria-label="Card art: girl with bicycle and hand-lettered words" style="background:linear-gradient(135deg,#f0c85a,#f6e7b4)"></div>
      <h3>Duis autem vel eum iriure</h3><p>Nam liber tempor cum soluta nob is eleifend option congue nihil.</p>
      <svg class="note" width="18" height="22"><path d="M5 2v14" stroke="#111" stroke-width="2"/><ellipse cx="5" cy="17" rx="4" ry="3" fill="#111"/><path d="M6 2c2 4 8 6 8 12" fill="none" stroke="#111" stroke-width="2"/></svg>
      <span class="price">€ 2.99</span>
    </article>
    <article class="abs product" style="left:530px;top:685px">
      <div class="art" role="img" aria-label="Card art: colourful patchwork with a red flower" style="background:linear-gradient(135deg,#f0b83a,#d9433c 50%,#6fb1d9)"></div>
      <h3>Duis autem vel eum iriure</h3><p>Nam liber tempor cum soluta nob is eleifend option congue nihil.</p>
      <svg class="note" width="18" height="22"><path d="M5 2v14" stroke="#111" stroke-width="2"/><ellipse cx="5" cy="17" rx="4" ry="3" fill="#111"/><path d="M6 2c2 4 8 6 8 12" fill="none" stroke="#111" stroke-width="2"/></svg>
      <span class="price">€ 2.99</span>
    </article>
    <article class="abs product" style="left:737px;top:685px">
      <div class="art" role="img" aria-label="Card art: nativity painting" style="background:linear-gradient(135deg,#3d4a6a,#a05a3a 60%,#d9c3a5)"></div>
      <h3>Duis autem vel eum iriure</h3><p>Nam liber tempor cum soluta nob is eleifend option congue nihil.</p>
      <svg class="note" width="18" height="22"><path d="M5 2v14" stroke="#111" stroke-width="2"/><ellipse cx="5" cy="17" rx="4" ry="3" fill="#111"/><path d="M6 2c2 4 8 6 8 12" fill="none" stroke="#111" stroke-width="2"/></svg>
      <span class="price">€ 2.99</span>
    </article>
    <article class="abs product" style="left:323px;top:995px">
      <div class="art" role="img" aria-label="Card art: teddy bear on a quilt" style="background:linear-gradient(135deg,#cfe0ee,#a9c4e0 60%,#e8e2d0)"></div>
      <h3>Duis autem vel eum iriure</h3><p>Nam liber tempor cum soluta nob is eleifend option congue nihil.</p>
      <svg class="note" width="18" height="22"><path d="M5 2v14" stroke="#111" stroke-width="2"/><ellipse cx="5" cy="17" rx="4" ry="3" fill="#111"/><path d="M6 2c2 4 8 6 8 12" fill="none" stroke="#111" stroke-width="2"/></svg>
      <span class="price">€ 2.99</span>
    </article>
    <article class="abs product" style="left:530px;top:995px">
      <div class="art" role="img" aria-label="Card art: bouquet of flowers on blue" style="background:linear-gradient(#2c4fd0,#2a5fe0 60%,#1e3fae)"></div>
      <h3>Duis autem vel eum iriure</h3><p>Nam liber tempor cum soluta nob is eleifend option congue nihil.</p>
      <svg class="note" width="18" height="22"><path d="M5 2v14" stroke="#111" stroke-width="2"/><ellipse cx="5" cy="17" rx="4" ry="3" fill="#111"/><path d="M6 2c2 4 8 6 8 12" fill="none" stroke="#111" stroke-width="2"/></svg>
      <span class="price">€ 2.99</span>
    </article>
    <article class="abs product" style="left:737px;top:995px">
      <div class="art" role="img" aria-label="Card art: birthday number eighteen with teddy bear" style="background:linear-gradient(135deg,#fbe3c8,#f5b98a 60%,#e8502e)"></div>
      <h3>Duis autem vel eum iriure</h3><p>Nam liber tempor cum soluta nob is eleifend option congue nihil.</p>
      <svg class="note" width="18" height="22"><path d="M5 2v14" stroke="#111" stroke-width="2"/><ellipse cx="5" cy="17" rx="4" ry="3" fill="#111"/><path d="M6 2c2 4 8 6 8 12" fill="none" stroke="#111" stroke-width="2"/></svg>
      <span class="price">€ 2.99</span>
    </article>
  </main>

  <footer class="abs footer">
    <div class="links">Terms and Conditions | Privacy Promise | FAQ's | Contact Us</div>
    <div class="copy">Copyright © 2010-2014. All Rights Reserved.</div>
    <div class="social" style="left:704px;background:#3a5a9a"></div>
    <div class="social" style="left:745px;background:#2a9ad6"></div>
    <div class="social" style="left:786px;background:#f07a1a"></div>
    <div class="social" style="left:827px;background:#d9261c"></div>
  </footer>
</div>
</body>
</html>
```